We need a web site design that is connected to Talbrook Roofing an American company, Veteran owned. Specializing in new roofs of all kinds, repair existing roofs and emergency roof repairs. located in the north Georgia mountains

Target Market(s)

homeowners end users, real estate, home owners insurance companies

Industry/Entity Type

roofing

Contact Information for Business Card

logo, Veteran owned, supports veteran charities, phone number ect

Font styles to use
Serif

Requirements
Should not have
• na

```html
<!DOCTYPE html>
<html lang="en">
<head>
<meta charset="utf-8">
<title>Talbrook Roofing – Business Card</title>
<link rel="stylesheet" href="https://fonts.googleapis.com/css2?family=Montserrat:wght@500;600;700;800&family=Poppins:wght@400;500&display=swap">
<style>
  :root {
    --bg: #b9b9b9;
    --red-deep: #b00808;
    --red: #d3301a;
    --orange: #e8773a;
    --gold: #f7d274;
    --gold-text: #e0a126;
    --brand-red: #d11f1f;
    --ink: #2b2b2b;
    --white: #ffffff;
    --badge: #1f3a6b;
  }
  * { box-sizing: border-box; margin: 0; padding: 0; }
  html, body { width: 1200px; height: 900px; overflow: hidden; }
  body {
    background: var(--bg);
    font-family: "Montserrat", sans-serif;
    position: relative;
  }
  .card {
    position: absolute;
    width: 620px;
    height: 354px;
    border-radius: 26px;
    overflow: hidden;
    box-shadow: 0 10px 24px rgba(0,0,0,0.28);
  }
  /* Front */
  .card-front {
    left: 60px; top: 70px;
    background: linear-gradient(200deg, var(--gold) 0%, var(--orange) 38%, var(--red) 70%, var(--red-deep) 100%);
  }
  .brand {
    display: flex;
    align-items: center;
    gap: 14px;
  }
  .brand-dot {
    width: 34px; height: 34px; border-radius: 50%;
  }
  .brand-name {
    font-weight: 800;
    text-transform: uppercase;
    letter-spacing: 2px;
    line-height: 1.05;
  }
  .card-front .brand {
    position: absolute; left: 150px; top: 104px;
  }
  .card-front .brand-dot { background: var(--gold); }
  .card-front .brand-name { color: var(--gold); font-size: 38px; }
  .tagline {
    position: absolute; left: 44px; bottom: 42px;
    color: var(--white);
    font-weight: 600;
    font-size: 14px;
    letter-spacing: 1.2px;
    line-height: 1.45;
    text-transform: uppercase;
  }
  /* Back */
  .card-back {
    left: 520px; top: 486px;
    background: var(--white);
  }
  .card-back .brand { position: absolute; left: 40px; top: 42px; }
  .card-back .brand-dot { background: var(--brand-red); }
  .card-back .brand-name { color: var(--brand-red); font-size: 30px; }
  .person { position: absolute; left: 40px; top: 150px; }
  .person-name {
    color: var(--gold-text); font-weight: 500; font-size: 22px;
    letter-spacing: 1.5px; text-transform: uppercase;
  }
  .person-role { color: var(--brand-red); font-weight: 500; font-size: 18px; }
  .contacts {
    position: absolute; left: 40px; top: 232px;
    list-style: none;
    font-family: "Poppins", sans-serif;
    font-size: 16px; color: var(--ink);
  }
  .contacts li { display: flex; align-items: center; gap: 10px; line-height: 1.65; }
  .contacts svg { width: 16px; height: 16px; fill: var(--brand-red); }
  .contacts .accent { color: var(--brand-red); }
  .address {
    position: absolute; right: 36px; top: 212px;
    text-align: right;
    font-family: "Poppins", sans-serif;
    font-size: 15px; color: var(--ink); line-height: 1.45;
  }
  .badge {
    position: absolute; right: 40px; top: 120px;
    width: 96px; height: 62px; border-radius: 8px;
    background: var(--badge);
  }
</style>
</head>
<body>
  <section class="card card-front">
    <div class="brand">
      <span class="brand-dot"></span>
      <span class="brand-name">Talbrook<br>Roofing</span>
    </div>
    <p class="tagline">Specializing in new roofs of all kinds, repair<br>existing roofs and emergency roof repairs</p>
  </section>

  <section class="card card-back">
    <div class="brand">
      <span class="brand-dot"></span>
      <span class="brand-name">Talbrook<br>Roofing</span>
    </div>
    <div class="badge" role="img" aria-label="Veteran owned badge"></div>
    <div class="person">
      <p class="person-name">Daniel Harlow</p>
      <p class="person-role">Managing Director</p>
    </div>
    <ul class="contacts">
      <li>
        <svg viewBox="0 0 24 24" aria-hidden="true"><path d="M6.6 10.8a15.1 15.1 0 0 0 6.6 6.6l2.2-2.2a1 1 0 0 1 1-.25 11.4 11.4 0 0 0 3.6.57 1 1 0 0 1 1 1V20a1 1 0 0 1-1 1A17 17 0 0 1 3 4a1 1 0 0 1 1-1h3.5a1 1 0 0 1 1 1c0 1.25.2 2.45.57 3.57a1 1 0 0 1-.25 1z"/></svg>
        044-555 010 274
      </li>
      <li>
        <svg viewBox="0 0 24 24" aria-hidden="true"><path d="M2 5h20v14H2z M4 7v.5l8 5 8-5V7l-8 5z" fill-rule="evenodd"/></svg>
        info@talbrookroof.com
      </li>
      <li>
        <svg viewBox="0 0 24 24" aria-hidden="true"><path d="M12 2a10 10 0 1 0 0 20 10 10 0 0 0 0-20zm6.9 9h-3a15 15 0 0 0-1.3-6A8 8 0 0 1 18.9 11zM12 4.1c.9 1.3 1.7 3.6 1.9 6.9h-3.8c.2-3.3 1-5.6 1.9-6.9zM9.4 5a15 15 0 0 0-1.3 6h-3A8 8 0 0 1 9.4 5zM5.1 13h3a15 15 0 0 0 1.3 6A8 8 0 0 1 5.1 13zM12 19.9c-.9-1.3-1.7-3.6-1.9-6.9h3.8c-.2 3.3-1 5.6-1.9 6.9zm2.6-.9a15 15 0 0 0 1.3-6h3a8 8 0 0 1-4.3 6z"/></svg>
        <span>www.<span class="accent">talbrookroof</span>.com</span>
      </li>
    </ul>
    <p class="address">421, Address line goes here<br>45452,Country Name</p>
  </section>
</body>
</html>
```